Business Card Design

Lotside Ledger is an online automotive resource on a national scale specifically targeting lease purchases for new cars. Our Online and app platform allow prospective lease clients to scan a window sticker while at a franchise dealership and instantly receive a lease quote at what we call the sweet spot. Lotside Ledger offers price transparency during the lease process to allow average people the confidence in the lease process and takes away any fear of the big franchise dealers.
Lotside ledger allows ordinary lease customers to know they are getting a low price lease and not overpaying. Never overpay again

Industry/Entity Type

Automotive

Contact Information for Business Card

Lotside Ledger
Marcus Todwell (President of operations)
Phone: 888-302-7716
Cell: 561-448-2053

```html
<!DOCTYPE html>
<html lang="en">
<head>
<meta charset="utf-8">
<title>Lotside Ledger — Business Card</title>
<link href="https://fonts.googleapis.com/css2?family=PT+Sans:ital,wght@0,400;0,700;1,400&display=swap" rel="stylesheet">
<style>
  :root {
    --page: #ffffff;
    --ink: #0a0a0a;
    --paper: #ffffff;
    --metal-light: #f1f4f5;
    --metal-mid: #d9dfe1;
    --metal-dark: #bfc8cb;
  }
  * { margin: 0; padding: 0; box-sizing: border-box; }
  html, body {
    width: 1000px; height: 1200px; overflow: hidden;
    background: var(--page);
    font-family: "PT Sans", Arial, sans-serif;
    color: var(--ink);
  }
  .canvas { position: relative; width: 1000px; height: 1200px; }

  .card { position: absolute; overflow: hidden; background: var(--paper); }
  .brushed-metal {
    position: absolute; left: 0; right: 0;
    background:
      linear-gradient(90deg, rgba(255,255,255,.5), rgba(190,200,203,.35) 30%, rgba(255,255,255,.6) 55%, rgba(200,208,210,.4) 80%, rgba(255,255,255,.5)),
      linear-gradient(180deg, var(--metal-light), var(--metal-mid) 50%, var(--metal-light));
  }
  .rule { position: absolute; height: 2px; background: var(--ink); }

  /* Front */
  .card-front { left: 193px; top: 187px; width: 640px; height: 361px; }
  .card-front .band { position: absolute; left: 0; right: 0; height: 71px; background: var(--ink); }
  .card-front .band-top { top: 0; }
  .card-front .band-bottom { bottom: 0; }
  .card-front .brushed-metal { top: 85px; height: 191px; }
  .wordmark {
    position: absolute; font-weight: 700; color: var(--ink);
    text-transform: uppercase; line-height: 1; white-space: nowrap;
  }
  .card-front .wordmark {
    left: 0; right: 0; top: 155px; text-align: center;
    font-size: 46px; letter-spacing: 1px;
  }

  /* Back */
  .card-back { left: 193px; top: 652px; width: 613px; height: 358px; }
  .card-back .brushed-metal { top: 0; bottom: 0; }
  .card-back .header-strip {
    position: absolute; left: 0; right: 0; top: 48px; height: 73px;
    background: var(--paper);
  }
  .card-back .header-strip .wordmark { left: 60px; top: 24px; font-size: 24px; }
  .person { position: absolute; right: 36px; top: 12px; text-align: right; }
  .person-name { font-size: 22px; font-weight: 400; line-height: 1.2; }
  .person-title { font-size: 13px; font-style: italic; line-height: 1.2; }
  .card-back .feature-name {
    position: absolute; left: 0; right: 0; top: 215px; text-align: center;
    font-size: 40px; letter-spacing: 1px;
  }
  .contact {
    position: absolute; top: 308px; font-size: 15px; font-weight: 700;
  }
  .contact-phone { left: 37px; }
  .contact-cell { right: 36px; }
</style>
</head>
<body>
<main class="canvas">

  <section class="card card-front" aria-label="Business card front">
    <div class="band band-top"></div>
    <div class="rule" style="top:80px; left:0; right:0;"></div>
    <div class="brushed-metal" role="img" aria-label="Brushed metal texture"></div>
    <div class="rule" style="top:117px; left:52px; width:515px;"></div>
    <span class="wordmark">Lotside Ledger</span>
    <div class="rule" style="top:242px; left:52px; width:515px;"></div>
    <div class="rule" style="top:278px; left:0; right:0;"></div>
    <div class="band band-bottom"></div>
  </section>

  <section class="card card-back" aria-label="Business card back">
    <div class="brushed-metal" role="img" aria-label="Brushed metal texture"></div>
    <div class="header-strip">
      <span class="wordmark">Lotside Ledger</span>
      <div class="person">
        <p class="person-name">Marcus Todwell</p>
        <p class="person-title">President of operations</p>
      </div>
    </div>
    <span class="wordmark feature-name">Lotside Ledger</span>
    <div class="rule" style="top:295px; left:0; right:0;"></div>
    <p class="contact contact-phone">Phone: 888-302-7716</p>
    <p class="contact contact-cell">Cell: 561-448-2053</p>
    <div class="rule" style="top:337px; left:0; right:0;"></div>
  </section>

</main>
</body>
</html>
```